Supplement Company Needs a Protein Powder Pouch Design

We are looking for a modern and fresh design for our 500g pouches of protein powder as our current design is not eye catching or exciting enough.

This new design will be printed on both sides of a 178mm x 280mm x 101mm pouch.

We have 4 flavours. These are Banana Ice Cream, Chocolate Deluxe, Strawberries & Cream and Vanilla Ice Cream.
Updates

Need extra days to review

Industry/Entity Type

Supplement

Requirements
Must have
• Attractive and eye catching front and space for all the nutritional information and ingredients on the back.

Must clearly state 'food supplement' somewhere on the front of the pouch.
Nice to have
• Our logo is attached.
Should not have
• No health claims as these are not allowed in the UK

```html
<!DOCTYPE html>
<html lang="en">
<head>
<meta charset="utf-8">
<title>BRAVO Supplements – Protein Powder Range</title>
<link href="https://fonts.googleapis.com/css2?family=Montserrat:wght@600;700;800&family=Roboto+Condensed:wght@700&display=swap" rel="stylesheet">
<style>
  :root {
    --ink: #262626;
    --paper: #ffffff;
    --pouch: #f7f7f7;
    --zip: #e2e2e2;
    --choc-band: #e3a57c;
    --choc-band-dark: #cf8a60;
    --choc-strip: #7b2f1b;
    --choc-art: #6e3b26;
    --straw-band: #dfaed0;
    --straw-band-dark: #c98ab5;
    --straw-strip: #c21a7c;
    --straw-art: #d9413f;
    --van-band: #b3dcf3;
    --van-band-dark: #95c9e9;
    --van-strip: #18a0dc;
    --van-art: #f5edc4;
    --ban-band: #f2c95c;
    --ban-band-dark: #e2ad3a;
    --ban-strip: #d9812b;
    --ban-art: #f7eab2;
  }
  * { box-sizing: border-box; margin: 0; padding: 0; }
  html, body { width: 1200px; height: 538px; overflow: hidden; background: var(--paper); }
  .range { position: relative; width: 1200px; height: 538px; }

  .pouch {
    position: absolute; top: 73px; width: 262px; height: 375px;
    background: var(--pouch);
    font-family: "Montserrat", sans-serif;
  }
  .pouch--chocolate { left: 40px;  --band: var(--choc-band);  --band-dark: var(--choc-band-dark);  --strip: var(--choc-strip);  --art: var(--choc-art); }
  .pouch--strawberry { left: 330px; --band: var(--straw-band); --band-dark: var(--straw-band-dark); --strip: var(--straw-strip); --art: var(--straw-art); }
  .pouch--vanilla { left: 620px; --band: var(--van-band);   --band-dark: var(--van-band-dark);   --strip: var(--van-strip);   --art: var(--van-art); }
  .pouch--banana { left: 910px; --band: var(--ban-band);   --band-dark: var(--ban-band-dark);   --strip: var(--ban-strip);   --art: var(--ban-art); }

  .pouch__zip { position: absolute; left: 12px; right: 12px; height: 2px; background: var(--zip); }
  .pouch__zip--upper { top: 56px; }
  .pouch__zip--lower { top: 66px; }

  .brand { position: absolute; top: 100px; left: 0; right: 0; text-align: center; color: var(--ink); }
  .brand__name { font-weight: 800; font-size: 46px; line-height: 1; letter-spacing: -1px; }
  .brand__tag { margin-top: 6px; font-weight: 700; font-size: 9px; letter-spacing: 7.6px; padding-left: 7px; }

  .band {
    position: absolute; top: 171px; left: 5px; right: 5px; bottom: 0;
    background: linear-gradient(90deg, var(--band-dark) 0%, var(--band) 55%, var(--band-dark) 100%);
  }
  .title { position: absolute; top: 12px; left: 0; right: 0; padding-left: 46px; }
  .title__kicker { color: var(--paper); font-weight: 700; font-size: 14.5px; line-height: 1; }
  .title__protein { color: var(--paper); font-weight: 800; font-size: 34px; line-height: 1; margin-top: 3px; }
  .title__powder { color: var(--ink); font-weight: 800; font-size: 34px; line-height: 1; margin-top: 1px; }

  .flavour {
    position: absolute; top: 99px; left: 0; right: 0; height: 33px; z-index: 2;
    background: var(--strip); color: var(--paper);
    padding: 5px 0 0 48px;
    font-weight: 700; font-size: 11px; line-height: 1.05;
  }
  .flavour-art {
    position: absolute; top: 134px; left: 166px; width: 76px; height: 56px; z-index: 1;
    border-radius: 45%;
    background: radial-gradient(circle at 50% 50%, var(--art) 0%, var(--art) 58%, transparent 72%);
  }
  .net-weight {
    position: absolute; top: 181px; left: 48px;
    font-family: "Roboto Condensed", sans-serif; font-weight: 700; font-size: 7px;
    color: rgba(60, 60, 60, 0.55);
  }
</style>
</head>
<body>
<main class="range">

  <section class="pouch pouch--chocolate">
    <div class="pouch__zip pouch__zip--upper"></div>
    <div class="pouch__zip pouch__zip--lower"></div>
    <div class="brand"><div class="brand__name">BRAVO</div><div class="brand__tag">SUPPLEMENTS</div></div>
    <div class="band">
      <div class="title"><div class="title__kicker">FOOD SUPPLEMENT</div><div class="title__protein">PROTEIN</div><div class="title__powder">POWDER</div></div>
      <div class="flavour">CHOCOLATE<br>DELUXE FLAVOUR</div>
      <div class="flavour-art" role="img" aria-label="Photo of broken milk chocolate pieces"></div>
      <div class="net-weight">Net Weight: 500g</div>
    </div>
  </section>

  <section class="pouch pouch--strawberry">
    <div class="pouch__zip pouch__zip--upper"></div>
    <div class="pouch__zip pouch__zip--lower"></div>
    <div class="brand"><div class="brand__name">BRAVO</div><div class="brand__tag">SUPPLEMENTS</div></div>
    <div class="band">
      <div class="title"><div class="title__kicker">FOOD SUPPLEMENT</div><div class="title__protein">PROTEIN</div><div class="title__powder">POWDER</div></div>
      <div class="flavour">STRAWBERRIES<br>&amp; CREAM FLAVOUR</div>
      <div class="flavour-art" role="img" aria-label="Photo of a halved fresh strawberry"></div>
      <div class="net-weight">Net Weight: 500g</div>
    </div>
  </section>

  <section class="pouch pouch--vanilla">
    <div class="pouch__zip pouch__zip--upper"></div>
    <div class="pouch__zip pouch__zip--lower"></div>
    <div class="brand"><div class="brand__name">BRAVO</div><div class="brand__tag">SUPPLEMENTS</div></div>
    <div class="band">
      <div class="title"><div class="title__kicker">FOOD SUPPLEMENT</div><div class="title__protein">PROTEIN</div><div class="title__powder">POWDER</div></div>
      <div class="flavour">VANILLA ICE CREAM<br>FLAVOUR</div>
      <div class="flavour-art" role="img" aria-label="Photo of a vanilla ice cream scoop with vanilla pods and flower"></div>
      <div class="net-weight">Net Weight: 500g</div>
    </div>
  </section>

  <section class="pouch pouch--banana">
    <div class="pouch__zip pouch__zip--upper"></div>
    <div class="pouch__zip pouch__zip--lower"></div>
    <div class="brand"><div class="brand__name">BRAVO</div><div class="brand__tag">SUPPLEMENTS</div></div>
    <div class="band">
      <div class="title"><div class="title__kicker">FOOD SUPPLEMENT</div><div class="title__protein">PROTEIN</div><div class="title__powder">POWDER</div></div>
      <div class="flavour">BANANA ICE CREAM<br>FLAVOUR</div>
      <div class="flavour-art" role="img" aria-label="Photo of a banana ice cream scoop with banana slices"></div>
      <div class="net-weight">Net Weight: 500g</div>
    </div>
  </section>

</main>
</body>
</html>
```